Harborline Crest Insurance Services

we are a high end insurance agency we specialize on Auto | Home | Business | Life looking for something professional and luxuries at the same time. if you guys need anything else please let me know.

Auto | Home | Business | Life must be under logo on the back with black background.

i want the back part to be black with our gold logo on it.

Target Market(s)

Auto | Home | Business | Life

Industry/Entity Type

Insurance Broker

Contact Information for Business Card

My logo is gold so a black in the back would be nice.

Font styles to use
Serif

Colors
000000

Requirements
Must have
• Big logo on the back with black background.

```html
<!DOCTYPE html>
<html lang="en">
<head>
<meta charset="utf-8">
<title>Harborline Crest Insurance Services – Business Card</title>
<link rel="stylesheet" href="https://fonts.googleapis.com/css2?family=Cinzel:wght@600&family=Playfair+Display:wght@700&family=Open+Sans:wght@400;600&display=swap">
<style>
  :root {
    --backdrop: #e9e6e2;
    --card-black: #1c1c1c;
    --card-white: #ffffff;
    --gold: #f2b81c;
    --silver: #a9a9ab;
    --ink: #2b2b2b;
    --muted: #3a3a3a;
    --shadow: rgba(0, 0, 0, 0.28);
  }
  * { margin: 0; padding: 0; box-sizing: border-box; }
  html, body {
    width: 1200px;
    height: 902px;
    overflow: hidden;
    background: var(--backdrop);
  }
  .canvas {
    position: relative;
    width: 1200px;
    height: 902px;
  }
  .card {
    position: absolute;
    width: 620px;
    height: 354px;
    box-shadow: 0 18px 40px var(--shadow);
  }
  /* Back of card */
  .card-back {
    left: 70px;
    top: 90px;
    background: var(--card-black);
    display: flex;
    flex-direction: column;
    align-items: center;
    justify-content: center;
    gap: 16px;
  }
  .brand-dot {
    width: 64px;
    height: 64px;
    border-radius: 50%;
    background: var(--gold);
  }
  .brand-name {
    font-family: "Cinzel", serif;
    font-weight: 600;
    color: var(--gold);
    text-align: center;
    line-height: 1.15;
  }
  .card-back .brand-name { font-size: 44px; }
  .card-back .brand-name span {
    display: block;
    font-size: 21px;
    letter-spacing: 0.32em;
  }
  .service-lines {
    font-family: "Cinzel", serif;
    font-weight: 600;
    font-size: 15px;
    letter-spacing: 0.18em;
    color: var(--silver);
    word-spacing: 0.2em;
  }
  /* Front of card */
  .card-front {
    left: 510px;
    top: 460px;
    background: var(--card-white);
    padding: 34px 44px;
  }
  .front-brand {
    display: flex;
    align-items: center;
    gap: 14px;
  }
  .front-brand .brand-dot { width: 34px; height: 34px; }
  .card-front .brand-name {
    font-size: 22px;
    text-align: left;
  }
  .card-front .brand-name span {
    display: block;
    font-size: 11px;
    letter-spacing: 0.3em;
  }
  .person { margin-top: 40px; }
  .person-name {
    font-family: "Playfair Display", serif;
    font-weight: 700;
    font-size: 34px;
    color: var(--ink);
    line-height: 1;
  }
  .person-title {
    font-family: "Open Sans", sans-serif;
    font-weight: 600;
    font-size: 14px;
    color: var(--gold);
    margin-left: 18px;
    margin-top: 2px;
  }
  .contact-list {
    list-style: none;
    margin-top: 26px;
    font-family: "Open Sans", sans-serif;
    font-size: 14px;
    color: var(--muted);
  }
  .contact-list li {
    display: flex;
    align-items: center;
    gap: 9px;
    height: 25px;
  }
  .contact-icon {
    width: 14px;
    height: 14px;
    flex: none;
  }
</style>
</head>
<body>
<main class="canvas">
  <section class="card card-back" aria-label="Card back">
    <div class="brand-dot" aria-hidden="true"></div>
    <p class="brand-name">Harborline Crest<span>Insurance Services</span></p>
    <p class="service-lines">Auto | Home | Business | Life</p>
  </section>

  <section class="card card-front" aria-label="Card front">
    <div class="front-brand">
      <div class="brand-dot" aria-hidden="true"></div>
      <p class="brand-name">Harborline Crest<span>Insurance Services</span></p>
    </div>

    <div class="person">
      <h1 class="person-name">Daniel Reyes</h1>
      <p class="person-title">general director</p>
    </div>

    <ul class="contact-list">
      <li>
        <svg class="contact-icon" viewBox="0 0 14 14" aria-hidden="true"><rect x="3.5" y="1" width="7" height="12" rx="1.2" fill="none" stroke="#f2b81c" stroke-width="1.3"/><circle cx="7" cy="11" r="0.8" fill="#f2b81c"/></svg>
        +1 555 204 7731
      </li>
      <li>
        <svg class="contact-icon" viewBox="0 0 14 14" aria-hidden="true"><text x="7" y="11.5" text-anchor="middle" font-family="Open Sans, sans-serif" font-size="13" font-weight="600" fill="#f2b81c">@</text></svg>
        hello@harborlinecrest.com
      </li>
      <li>
        <svg class="contact-icon" viewBox="0 0 14 14" aria-hidden="true"><g fill="none" stroke="#f2b81c" stroke-width="1.1"><circle cx="7" cy="7" r="5.8"/><ellipse cx="7" cy="7" rx="2.6" ry="5.8"/><line x1="1.2" y1="7" x2="12.8" y2="7"/></g></svg>
        www.harborlinecrest.com
      </li>
      <li>
        <svg class="contact-icon" viewBox="0 0 14 14" aria-hidden="true"><rect x="1" y="3" width="12" height="8.5" fill="#f2b81c"/><polyline points="1,3 7,8 13,3" fill="none" stroke="#ffffff" stroke-width="1.1"/></svg>
        PO Box 41820 Bayview, North Place, CA, USA
      </li>
    </ul>
  </section>
</main>
</body>
</html>
```